Harbor Light Church San Francisco needs a Leadership Booklet designed.

We need a Leadership Booklet to be designed and formatted. The content is currently 27 pages and involves headings, quotes, bolded statements and scripture that we would like to stick out. We also need a cover designed for it as well. Cover - "Harbor Light Leadership Development"

Here is a link to our Harbor Light Church style guide.
https://studio-51832.brandvault-example.com/d/7QwRnBzK2Lp9/harbor-light-church-style-guide

Target Market(s)

Leaders within our church.

Font styles to use
Sans Serif

```html
<!DOCTYPE html>
<html lang="en">
<head>
<meta charset="utf-8">
<title>Harbor Light Leadership Development – Booklet Spreads</title>
<link href="https://fonts.googleapis.com/css2?family=Cabin:wght@600&family=Lato:wght@300;400;700&display=swap" rel="stylesheet">
<style>
  :root{
    --bg:#ebecee;
    --page:#ffffff;
    --ink:#2b2b2b;
    --ink-soft:#3a3a3a;
    --pill:#5a5a5a;
    --green:#6abf4b;
    --tint:rgba(150,205,120,.28);
  }
  *{box-sizing:border-box;margin:0;padding:0}
  html,body{width:844px;height:1200px;overflow:hidden;background:var(--bg)}
  body{position:relative;font-family:"Lato",sans-serif;color:var(--ink)}
  .divider{position:absolute;left:0;top:595px;width:844px;height:2px;background:#fff}
  .page-label{position:absolute;width:356px;text-align:center;font:400 14px/1 "Lato",sans-serif;color:#222}
  .page{position:absolute;width:356px;height:505px;background:var(--page);
        box-shadow:3px 4px 7px rgba(0,0,0,.28);overflow:hidden}
  .page-body{position:absolute;left:41px;width:275px;font-size:6.8px;line-height:9.1px;font-weight:300;color:var(--ink-soft)}
  .page-body.justify p,.page-body.justify li{text-align:justify}
  .page-body p{margin-bottom:7.5px}
  .lead-in{margin-bottom:0!important}
  .strong{font-weight:700;color:#1e1e1e}
  .callout{font-weight:700;color:#1e1e1e;margin-left:-5px;margin-right:-28px;padding:2px 28px 2px 5px;
           background:linear-gradient(90deg,var(--tint),rgba(150,205,120,0) 95%)}
  .list{margin-bottom:7.5px}
  .bullets{list-style:none;margin-bottom:7.5px}
  .bullets li{position:relative;padding-left:9px;margin-bottom:7.5px}
  .bullets li::before{content:"";position:absolute;left:0;top:3px;width:3.5px;height:3.5px;border-radius:50%;background:#333}
  .section-pill{position:absolute;left:78px;top:29px;width:200px;height:30px;border-radius:15px;background:var(--pill);
        color:#fff;font:600 17px/30px "Cabin",sans-serif;text-align:center}
  .rules{position:absolute;left:0;top:468px;width:314px}
  .rules span{display:block;height:3px;background:var(--green);margin-bottom:5px}
</style>
</head>
<body>
  <div class="divider"></div>

  <div class="page-label" style="left:54px;top:17px">Pg-3</div>
  <div class="page-label" style="left:434px;top:17px">Pg-4</div>
  <div class="page-label" style="left:54px;top:623px">Pg-5</div>
  <div class="page-label" style="left:434px;top:623px">Pg-6</div>

  <!-- Page 3 -->
  <section class="page" style="left:54px;top:42px">
    <h1 class="section-pill">Who Harbor Light Leaders Are</h1>
    <div class="page-body" style="top:75px">
      <p class="callout">As Christian leaders, never forget this:<br>WE ARE FOLLOWERS BEFORE WE ARE LEADERS.</p>
      <p>Before we lead others, let’s make sure we are orienting our entire lives around Jesus. We can’t give others what we lack ourselves. Never forget what Jesus said in John 15:5, “I am the vine; you are the branches. If you remain in me and I in you, you will bear much fruit; apart from me you can do nothing.”</p>
      <p>One of the greatest leadership lessons we can learn from watching other leaders throughout the world is this:</p>
      <p class="callout">It is dangerous to have an outer life that your inner life cannot keep up with.</p>
      <p>“One of the great and subtle temptations of leadership is to neglect the inner life and your relationship with God because of the many things which demand immediate attention.” - Samuel Crane, The Gift of Leading</p>
      <p>“Because my inner life is invisible, it is easy to neglect.” - Jonah Ortley, Soul Tending</p>
      <p>“The most important thing in your life is not what you do; it’s who you become.” - Dalton Wheeler</p>
      <p class="callout">Philippians 1:6 being confident of this, that he who began a good work in you will carry it on to completion until the day of Christ Jesus.</p>
      <p class="callout">Galatians 4:19 My dear children, for whom I am again in the pains of childbirth until Christ is FORMED in you</p>
      <p>Christian leadership certainly has a lot to do with the work that we do for God and we’ll get there in the next section. We’re mostly interested in what we can produce in this world, but God is mostly interested in what He can produce in us. Here’s a question we should ask:</p>
      <p class="callout">How can I position myself so that God can do His work in me?</p>
      <p class="callout">Luke 6:43-45 “No good tree bears bad fruit, nor does a bad tree bear good fruit. 44 Each tree is recognized by its own fruit. People do not pick figs from thornbushes, or grapes from briers. 45 A good man brings good things out of the good stored up in his heart, and an evil man brings evil things out of the evil stored up in his heart. For the mouth speaks what the heart is full of.</p>
    </div>
    <div class="rules"><span></span><span></span><span></span></div>
  </section>

  <!-- Page 4 -->
  <section class="page" style="left:434px;top:42px">
    <div class="page-body justify" style="top:43px">
      <p>At the end of the day, what goes into us is what comes out of us. We can only give this world the person we truly are. And if we don’t fill ourselves with the right things, it will affect us and those we lead.</p>
      <p>This is where spiritual practices (also called “spiritual disciplines”) come into play. One of the best books on spiritual practices is The Practice of Discipline by Richard Fenwick. It is a great resource to learn more about the various practices. Harbor Light did a teaching series on spiritual practices called Formed that you can access on the media page of our website.</p>
      <p>For our purposes here, this is a list of some of the spiritual practices we want to pursue as Harbor Light Leaders:</p>
      <p class="list">Scripture and Prayer (These are primary and something we should be engaged in daily.)<br>Silence<br>Solitude<br>Fasting<br>Worship<br>Sabbath</p>
      <p>There are several books that speak to the inner life of a leader. One of those books is The Quiet Minister by Ivan Cole. Below are some quotes from this book:</p>
      <p>“I would only be able to sustain the work to which I knew I had been called if I lived each day in active dependence and trust in God.”</p>
      <p>“The value of what we do will flow directly from who we are.”</p>
      <p>“In such demanding contexts, unless we are deeply sustained by the resources which only Christ can give us, we are all too likely to lose our way, and perhaps even lose our vocation.”</p>
      <p>“God meets us where we are, not where we would like to be or where we would like other people to think we are.”</p>
      <p>“Putting first things first in ministry means that we make the nurture of our relationship with God the priority of our lives.”</p>
      <p>One of the things most driven leaders overlook is their need for rest and replenishment. We tend to wear busyness as a badge of honor and that has to stop if we are going to be the kind of leaders God intends for us to be. The Sabbath Within by Marcus Bell is a book that can help us pay attention to the part of life we often ignore the most. Here are some quotes and additional thoughts from this resource:</p>
    </div>
    <div class="rules"><span></span><span></span><span></span></div>
  </section>

  <!-- Page 5 -->
  <section class="page" style="left:54px;top:648px">
    <div class="page-body justify" style="top:42px">
      <p>“One measure for whether or not you’re rested enough – besides falling asleep in board meetings – is to ask yourself this: How much do I care about the things I care about? When we lose concern for people, both the lost and the found, for the bride of Christ, for friendship, for truth and beauty and goodness; when we cease to laugh when our children laugh (and instead yell at them to quiet down) or weep when our spouses weep (and instead wish they didn’t get so emotional); when we hear news of trouble among our neighbors and our first thought is that we hope it isn’t going to involve us – when we stop caring about the things we care about – that’s a signal we’re too busy. We have let ourselves be consumed by the things that feed the ego but starve the soul.”</p>
      <p>Don’t miss the last sentence; reread it. So many leaders have fallen because of they focused on the ego part and neglected to take care of their souls.”</p>
      <p>“Busyness kills the heart. Busyness makes us stop caring about the things we care about. And not only that. Busyness also robs us of knowing God the way we might.”</p>
      <p>Being constantly busy is not a sign that you are a great leader; it’s a sign that the opposite is likely true.</p>
      <p>“A common characteristic of driven people is that, at some point, they forget the purpose. They lose the point. The very reason they began something – embarked on a journey, undertook a project, waged a war, entered a profession, married a girl – erodes under the weight of their striving. Their original inspiration may be noble. But driven too hard, it gets supplanted by greed for more, or dread of setback, or force of habit.”</p>
      <p class="callout" style="font-weight:400">Questions to ponder in light of this quote: <span class="strong">Why did you first get into serving and leading? What would it look like to get back to that reason?</span></p>
      <p>“If God works all things together for good for those who love him and are called to his purposes, you can relax. If he doesn’t, start worrying. If God can take any mess, any mishap, any wastage, any wreckage, any anything, and choreograph beauty and meaning from it, then you can take a day off. If he can’t, get busy. Either God’s always at work, watching the city, building the house, or you need to try harder. Either God is good and in control, or it all depends on you.”</p>
      <p>This last quote is a reminder of a Scripture that became the foundation for how Harbor Light Church started. These were the two verses shared at Harbor Light’s very first meeting in 2010, which was attended by 13 people in a living room.</p>
    </div>
    <div class="rules"><span></span><span></span><span></span></div>
  </section>

  <!-- Page 6 -->
  <section class="page" style="left:434px;top:648px">
    <div class="page-body justify" style="top:33px">
      <p class="callout">Psalm 127:1-2 Unless the LORD builds the house, the builders labor in vain. Unless the LORD watches over the city, the guards stand watch in vain. In vain you rise early and stay up late, toiling for food to eat - for he grants sleep to those he loves.</p>
      <p>God is limitless; we are not. God created us to rest, to be refilled, to be replenished. And if we don’t pay attention to the rhythms He intends for us to adhere to, we will pay a price and so will the people we are called to lead.</p>
      <p class="callout">The best thing you bring to the table is a filled bucket and a heart that is right with God.</p>
      <p>Jesus models this so well for us in Mark 1:29-37. Read the entire text on your own, but let’s look at a few things that we see him do:</p>
      <ul class="bullets">
        <li>Jesus is doing ministry in this setting. He heals Peter’s mother-in-law. That same evening, they brought to Jesus all the sick and demon-possessed. Here’s what the text actually says happened - “The WHOLE town gathered at the door, and Jesus healed many who had various diseases. He also drove out many demons…”</li>
        <li>So Jesus has been doing a lot. At this point, many leaders would be so addicted to the adrenaline that comes with these results or they would convince themselves that everyone needs them at all times. Would Jesus follow this same pattern?</li>
        <li>Mark 1:35 - “Very early in the morning, while it was STILL DARK, Jesus got up, LEFT the house and went off to a SOLITARY place, where he PRAYED.” Jesus calls a timeout from all of the leading He had been doing. Why? He needed to be alone with his Heavenly Father. His soul needed to be filled up again before he was ready to step back into all that he would need to do next.</li>
        <li>Notice this from Mark 1:36-37: “Simon and his companions went to look for him (Jesus), and when they found him, they exclaimed: ‘Everyone is looking for you!’” Jesus knew what it was like to have incredible demands placed on his life by others. That didn’t matter to him. He knew what was needed if he was going to continue taking care of the people he had been sent to lead. If Jesus needed to take the time away, why would we think that we can just keep producing without doing the same?</li>
      </ul>
      <p>Here’s another occasion where we see Jesus do something similar:</p>
      <p class="callout">Luke 5:15-16 Yet the news about him spread all the more, so that the crowds of people came to hear him and to be healed of their sicknesses. But Jesus OFTEN withdrew to lonely places and prayed.</p>
      <p>*How are you moving between engagement and disengagement? Time with the people you lead and time alone? If Jesus did this often, it probably won’t be sufficient for us to only do it occasionally.</p>
    </div>
    <div class="rules"><span></span><span></span><span></span></div>
  </section>
</body>
</html>
```